Business Card Design using new attached logo

We are a family run Plumbing and Heating firm looking to improve our company image with an improved business card and new logo.We are looking to keep the company colour (Blue) involved in our design

Reason: New logo added which needs to be incorporated on designs

Industry/Entity Type

Business

Contact Information for Business Card

See attachment of all info required.

Requirements
Must have
• We have just picked a new company logo which is attached.
• Could you please provide your business card designs using this logo.
• We are looking for the logo on the back as well as the front with all the info required

```html
<!DOCTYPE html>
<html lang="en">
<head>
<meta charset="utf-8">
<title>Kestrel services ltd – Business Card</title>
<link rel="stylesheet" href="https://fonts.googleapis.com/css2?family=Exo+2:wght@400;500;600;700&display=swap">
<style>
  :root {
    --brand-blue: #213f94;
    --text-blue: #23409a;
    --label-grey: #7d8db5;
    --paper-light: #ffffff;
    --paper-shade: #e4e4e6;
    --divider: #b9bac0;
    --white: #ffffff;
  }
  html, body {
    margin: 0;
    padding: 0;
    overflow: hidden;
    background: var(--paper-light);
  }
  .card {
    position: relative;
    width: 1200px;
    height: 790px;
    overflow: hidden;
    font-family: "Exo 2", sans-serif;
    background: linear-gradient(100deg, var(--paper-light) 30%, #f3f3f4 65%, var(--paper-shade) 100%);
  }
  .divider {
    position: absolute;
    left: 418px;
    top: 205px;
    width: 5px;
    height: 442px;
    background: linear-gradient(to bottom, rgba(185,186,192,0) 0%, var(--divider) 40%, var(--divider) 85%, rgba(185,186,192,0.3) 100%);
  }
  .person {
    position: absolute;
    left: 86px;
    top: 360px;
    width: 320px;
  }
  .person-name {
    margin: 0;
    font-size: 41px;
    font-weight: 700;
    color: var(--text-blue);
    letter-spacing: 0.5px;
    line-height: 1;
    white-space: nowrap;
  }
  .person-role {
    margin: 12px 0 0;
    font-size: 27px;
    font-weight: 400;
    color: var(--label-grey);
    line-height: 1;
  }
  .contact {
    position: absolute;
    left: 448px;
    top: 266px;
    color: var(--text-blue);
  }
  .address {
    margin: 0;
    font-size: 26px;
    font-weight: 500;
    line-height: 38px;
    text-transform: uppercase;
  }
  .contact-line {
    margin: 0;
    font-size: 32px;
    font-weight: 400;
    line-height: 46px;
    white-space: nowrap;
  }
  .contact-line .label { color: var(--label-grey); }
  .contact-line .value { color: var(--text-blue); }
  .contact-line.fax { padding-left: 8px; }
  .contact-gap { height: 44px; }
  .email .value { font-size: 31px; }
  .footer-band {
    position: absolute;
    left: 0;
    bottom: 0;
    width: 1200px;
    height: 140px;
    background: var(--brand-blue);
  }
  .company {
    position: absolute;
    left: 782px;
    top: 669px;
    display: flex;
    align-items: flex-start;
    gap: 10px;
  }
  .company-square {
    width: 71px;
    height: 71px;
    background: var(--white);
  }
  .company-name {
    margin-top: 2px;
    font-size: 30px;
    font-weight: 500;
    color: var(--white);
    line-height: 1;
    white-space: nowrap;
  }
</style>
</head>
<body>
  <main class="card">
    <div class="divider"></div>

    <section class="person">
      <h1 class="person-name">MARK HOLLAND</h1>
      <p class="person-role">Director</p>
    </section>

    <section class="contact">
      <p class="address">14 Mill Parade,<br>Elmstead Road, Ashford, Kent TN2 7LP</p>
      <p class="contact-line telephone"><span class="label">Telephone:</span> <span class="value">020 7946 0213</span></p>
      <p class="contact-line fax"><span class="label">Fax:</span> <span class="value">020 7946 0458</span></p>
      <div class="contact-gap"></div>
      <p class="contact-line mobile"><span class="label">Mobile:</span> <span class="value">07700 900482</span></p>
      <p class="contact-line email"><span class="label">Email:</span> <span class="value">markholland@kestrelservices.co.uk</span></p>
    </section>

    <footer class="footer-band"></footer>
    <div class="company">
      <div class="company-square"></div>
      <span class="company-name">Kestrel services ltd</span>
    </div>
  </main>
</body>
</html>
```